Business Card Design

5* Hotel Property based on an island in Greece

My position is aparta from being a director, i'm on the accounts payable too, not sure how this should be stated, with a comma or "/"?

Sorry about the uploaded logo, it was a mistaken one!

There's also need to be added this  www.corvanteholdings.com on the back side of the card!

Also need to have the logo of the corvante holdings which can be found in a second on the brief! Thank you guys, irini

Industry/Entity Type

Business

Contact Information for Business Card

VERISTOKA PELLA Hotel
Irini Dravetsou
Director, AP Dept.

www.veristoka.gr
Peltira Island 85300
Greece

irinidravetsou@fenmail.com
+306951273064

```html
<!DOCTYPE html>
<html lang="en">
<head>
<meta charset="utf-8">
<title>Veristoka Pella Hotel – Business Cards</title>
<link rel="stylesheet" href="https://fonts.googleapis.com/css2?family=PT+Sans:wght@400&family=Sorts+Mill+Goudy&display=swap">
<style>
  :root {
    --canvas-bg: #e8e8e8;
    --frosted-grey: #7c7c7c;
    --navy-deep: #0a1634;
    --navy-mid: #142a5c;
    --ocean-light: #2f6fbf;
    --mark-blue: #2aa7e8;
    --text-white: #ffffff;
    --text-soft: #dfe6f2;
    --gold: #e2a928;
    --ornament-light: rgba(170, 200, 240, 0.35);
    --ornament-green: rgba(110, 190, 60, 0.55);
  }
  html, body {
    margin: 0;
    padding: 0;
    width: 1000px;
    height: 1200px;
    overflow: hidden;
    background: var(--canvas-bg);
  }
  .canvas {
    position: relative;
    width: 1000px;
    height: 1200px;
  }
  .card {
    position: absolute;
    left: 190px;
    width: 620px;
    height: 360px;
    border-radius: 16px;
    overflow: hidden;
    color: var(--text-white);
    box-shadow: 0 4px 14px rgba(0,0,0,0.12);
  }
  .card--frosted { top: 30px; background: var(--frosted-grey); }
  .card--front {
    top: 420px;
    border-radius: 4px;
    background:
      radial-gradient(ellipse 75% 90% at 10% 100%, var(--ocean-light) 0%, rgba(47,111,191,0) 70%),
      linear-gradient(160deg, var(--navy-deep) 0%, var(--navy-mid) 55%, #1d4a92 100%);
  }
  .card--back {
    top: 810px;
    border-radius: 4px;
    background:
      radial-gradient(ellipse 70% 90% at 5% 100%, var(--ocean-light) 0%, rgba(47,111,191,0) 70%),
      linear-gradient(165deg, var(--navy-deep) 0%, var(--navy-mid) 60%, #1d4a92 100%);
  }

  /* hotel name lockup */
  .brand { position: absolute; left: 60px; top: 30px; }
  .brand__dot {
    position: absolute; left: 0; top: 4px;
    width: 58px; height: 58px; border-radius: 50%;
    background: var(--mark-blue);
  }
  .brand__name {
    position: absolute; left: 70px; top: 0;
    margin: 0;
    font-family: "PT Sans", sans-serif;
    font-weight: 400;
    font-size: 28px;
    line-height: 29px;
    letter-spacing: 0.5px;
    color: var(--text-white);
    white-space: nowrap;
  }
  .brand__web {
    position: absolute; left: 70px; top: 70px;
    margin: 0;
    font-family: "Sorts Mill Goudy", serif;
    font-size: 21px;
    color: var(--text-white);
    white-space: nowrap;
  }
  .brand--small { left: 36px; top: 24px; }
  .brand--small .brand__dot { width: 40px; height: 40px; top: 2px; }
  .brand--small .brand__name { left: 50px; font-size: 20px; line-height: 21px; }

  /* person */
  .person { position: absolute; right: 56px; top: 152px; text-align: right; }
  .person__name {
    margin: 0;
    font-family: "Sorts Mill Goudy", serif;
    font-weight: 400;
    font-size: 31px;
    line-height: 36px;
    color: var(--text-white);
  }
  .person__role {
    margin: 2px 0 0;
    font-family: "PT Sans", sans-serif;
    font-style: italic;
    font-size: 15px;
    color: var(--text-soft);
  }

  /* contact lines */
  .contact {
    position: absolute; left: 322px; top: 258px;
    margin: 0; padding: 0; list-style: none;
    font-family: "Sorts Mill Goudy", serif;
    font-size: 15px;
    color: var(--text-soft);
  }
  .contact__item { display: flex; align-items: center; height: 28px; }
  .contact__icon { width: 14px; height: 14px; margin-right: 16px; fill: var(--gold); flex: none; }

  /* ornament placeholders */
  .ornament { position: absolute; }
  .ornament--swirl-top {
    right: 0; top: 0; width: 210px; height: 130px;
    background: radial-gradient(ellipse at 70% 35%, var(--ornament-light) 0%, rgba(170,200,240,0) 70%);
  }
  .ornament--swirl-bottom {
    left: 0; bottom: 0; width: 240px; height: 180px;
    background: radial-gradient(ellipse at 35% 65%, var(--ornament-light) 0%, rgba(170,200,240,0) 70%);
  }
  .ornament--mosaic {
    left: 250px; top: 20px; width: 300px; height: 200px;
    background: radial-gradient(ellipse at 55% 45%, rgba(190,215,250,0.45) 0%, rgba(60,130,220,0.3) 40%, rgba(60,130,220,0) 72%);
  }
  .ornament--bubbles {
    left: 60px; top: 190px; width: 260px; height: 150px;
    background: radial-gradient(ellipse at 50% 50%, rgba(170,200,240,0.18) 0%, rgba(170,200,240,0) 70%);
  }
  .ornament--leaf-dots {
    right: 0; top: 0; width: 110px; height: 110px;
    background: radial-gradient(circle at 80% 25%, var(--ornament-green) 0%, rgba(110,190,60,0) 65%);
  }
</style>
</head>
<body>
<main class="canvas">

  <!-- frosted front -->
  <section class="card card--frosted" aria-label="Frosted card, front">
    <div class="brand">
      <span class="brand__dot"></span>
      <p class="brand__name">VERISTOKA<br>PELLA HOTEL</p>
      <p class="brand__web">www.veristoka.gr</p>
    </div>
    <div class="person">
      <h1 class="person__name">Irini Dravetsou</h1>
      <p class="person__role">Director , AP Dept.</p>
    </div>
    <ul class="contact">
      <li class="contact__item">
        <svg class="contact__icon" viewBox="0 0 14 14"><path d="M7 0a5 5 0 0 0-5 5c0 3.6 5 9 5 9s5-5.4 5-9a5 5 0 0 0-5-5zm0 7a2 2 0 1 1 0-4 2 2 0 0 1 0 4z"/></svg>
        Peltira Island,85300,Greece
      </li>
      <li class="contact__item">
        <svg class="contact__icon" viewBox="0 0 14 14"><path d="M0 3h14v9H0z M0 3l7 5 7-5" fill-rule="evenodd"/></svg>
        irinidravetsou@fenmail.com
      </li>
      <li class="contact__item">
        <svg class="contact__icon" viewBox="0 0 14 14"><path d="M3 0l2.5 3-1.5 2c.8 2 2.2 3.4 4.5 4.5l2-1.5 3 2.5-2 3C5.5 13 1 8.5 0 2.5z"/></svg>
        +306951273064
      </li>
    </ul>
  </section>

  <!-- blue front -->
  <section class="card card--front" aria-label="Blue card, front">
    <div class="ornament ornament--swirl-top" role="img" aria-label="Light blue swirl ornament"></div>
    <div class="ornament ornament--swirl-bottom" role="img" aria-label="Light blue swirl ornament with dotted arc and bubbles"></div>
    <div class="brand">
      <span class="brand__dot"></span>
      <p class="brand__name">VERISTOKA<br>PELLA HOTEL</p>
      <p class="brand__web">www.veristoka.gr</p>
    </div>
    <div class="person">
      <h2 class="person__name">Irini Dravetsou</h2>
      <p class="person__role">Director , AP Dept.</p>
    </div>
    <ul class="contact">
      <li class="contact__item">
        <svg class="contact__icon" viewBox="0 0 14 14"><path d="M7 0a5 5 0 0 0-5 5c0 3.6 5 9 5 9s5-5.4 5-9a5 5 0 0 0-5-5zm0 7a2 2 0 1 1 0-4 2 2 0 0 1 0 4z"/></svg>
        Peltira Island,85300,Greece
      </li>
      <li class="contact__item">
        <svg class="contact__icon" viewBox="0 0 14 14"><path d="M0 3h14v9H0z M0 3l7 5 7-5" fill-rule="evenodd"/></svg>
        irinidravetsou@fenmail.com
      </li>
      <li class="contact__item">
        <svg class="contact__icon" viewBox="0 0 14 14"><path d="M3 0l2.5 3-1.5 2c.8 2 2.2 3.4 4.5 4.5l2-1.5 3 2.5-2 3C5.5 13 1 8.5 0 2.5z"/></svg>
        +306951273064
      </li>
    </ul>
  </section>

  <!-- blue back -->
  <section class="card card--back" aria-label="Blue card, back">
    <div class="ornament ornament--mosaic" role="img" aria-label="Mosaic of outlined squares and blue dots"></div>
    <div class="ornament ornament--bubbles" role="img" aria-label="Rising bubbles"></div>
    <div class="ornament ornament--leaf-dots" role="img" aria-label="Green dotted accent"></div>
    <div class="brand brand--small">
      <span class="brand__dot"></span>
      <p class="brand__name">VERISTOKA<br>PELLA HOTEL</p>
    </div>
  </section>

</main>
</body>
</html>
```